I need new business cards designed

I would like to get some new designs on business cards. I will upload my logo for reference. The business cards that were designed for me a few months ago were too difficult for the print companies to work with. My company is Brivoldex.com LLC. It is an art company that sells painting and expression cards online.

```html
<!DOCTYPE html>
<html lang="en">
<head>
<meta charset="utf-8">
<title>Brivoldex.com business cards</title>
<link href="https://fonts.googleapis.com/css2?family=Montserrat:wght@700&family=Open+Sans:wght@400;600&display=swap" rel="stylesheet">
<style>
  :root{
    --backdrop:#4a4a4a;
    --card:#161616;
    --edge:#0aa0dc;
    --brand-indigo:#3b3f8f;
    --accent-blue:#0aa0dc;
    --text-light:#f2f2f2;
    --text-muted:#d8d8d8;
    --faint-panel:#1f1d1d;
  }
  *{box-sizing:border-box;margin:0;padding:0}
  html,body{width:1200px;height:801px;overflow:hidden}
  body{background:var(--backdrop);font-family:"Open Sans",Arial,sans-serif;position:relative}
  .card{
    position:absolute;top:246px;width:540px;height:309px;
    background:var(--card);border-radius:18px;
    border-left:3px solid var(--edge);border-bottom:3px solid var(--edge);
    overflow:hidden;
  }
  .card--front{left:45px}
  .card--back{left:615px}

  .brand{position:absolute;display:flex;align-items:center;gap:10px}
  .brand__mark{display:block;background:var(--accent-blue)}
  .brand__name{color:var(--brand-indigo);font-weight:600;white-space:nowrap}

  .card--front .brand{left:24px;top:24px}
  .card--front .brand__mark{width:28px;height:28px}
  .card--front .brand__name{font-size:21px}

  .faint-panel{
    position:absolute;left:300px;top:22px;width:215px;height:190px;
    background:linear-gradient(135deg,#1d1c1c,#221e1e 50%,#1b1c22);
  }
  .edge-tab{position:absolute;right:0;top:46px;width:7px;height:34px;background:var(--accent-blue)}

  .holder{position:absolute;right:30px;top:82px;text-align:right}
  .holder__name{font-family:"Montserrat",Arial,sans-serif;font-weight:700;font-size:22px;color:var(--accent-blue);letter-spacing:.2px}
  .holder__role{font-size:13px;color:var(--text-light);margin-top:2px}

  .address{position:absolute;left:70px;top:128px;font-size:13.5px;line-height:20px;color:var(--text-light)}

  .contact{position:absolute;left:70px;top:212px;list-style:none;font-size:12.5px;line-height:21px;color:var(--text-muted)}
  .contact li{display:flex;align-items:center;gap:7px}
  .contact svg{width:12px;height:12px;fill:var(--accent-blue);flex:none}

  .social{position:absolute;right:30px;bottom:26px;display:flex;gap:8px}
  .social span{width:13px;height:13px;border-radius:50%;background:var(--accent-blue)}

  .card--back .brand{left:70px;top:118px;gap:18px}
  .card--back .brand__mark{width:72px;height:72px}
  .card--back .brand__name{font-size:46px}
</style>
</head>
<body>
  <section class="card card--front" aria-label="Business card front">
    <div class="faint-panel" role="img" aria-label="Faint enlarged brand graphic in dark tones"></div>
    <div class="edge-tab"></div>
    <div class="brand">
      <span class="brand__mark"></span>
      <span class="brand__name">Brivoldex.com</span>
    </div>
    <div class="holder">
      <p class="holder__name">Daniel Reed Ashcombe</p>
      <p class="holder__role">CEO and Creator</p>
    </div>
    <address class="address" style="font-style:normal">
      218 West Marlow Ave.<br>Suite 140-2271
    </address>
    <ul class="contact">
      <li><svg viewBox="0 0 24 24"><path d="M6.6 10.8a15.1 15.1 0 0 0 6.6 6.6l2.2-2.2c.3-.3.7-.4 1-.2 1.1.4 2.3.6 3.6.6.6 0 1 .4 1 1V20c0 .6-.4 1-1 1A17 17 0 0 1 3 4c0-.6.4-1 1-1h3.5c.6 0 1 .4 1 1 0 1.3.2 2.5.6 3.6.1.3 0 .7-.2 1z"/></svg>555-014-2290</li>
      <li><svg viewBox="0 0 24 24"><path d="M2 5h20v14H2zm2 2v.5l8 5 8-5V7l-8 5z"/></svg>danielashcombe@brivoldex.com</li>
      <li><svg viewBox="0 0 24 24"><path d="M12 2a10 10 0 1 0 0 20 10 10 0 0 0 0-20zm0 2c1 0 2.4 2.2 2.8 6H9.2C9.6 6.2 11 4 12 4zm-2.8 8h5.6c-.4 3.8-1.8 6-2.8 6s-2.4-2.2-2.8-6zM4.1 12h3.1c.1 2.3.6 4.3 1.3 5.7A8 8 0 0 1 4.1 12zm12.7 0h3.1a8 8 0 0 1-4.4 5.7c.7-1.4 1.2-3.4 1.3-5.7zM4.1 10a8 8 0 0 1 4.4-5.7C7.8 5.7 7.3 7.7 7.2 10zm12.7 0c-.1-2.3-.6-4.3-1.3-5.7A8 8 0 0 1 19.9 10z"/></svg>www.Brivoldex.com</li>
    </ul>
    <div class="social" aria-label="Social profiles"><span></span><span></span><span></span></div>
  </section>

  <section class="card card--back" aria-label="Business card back">
    <div class="brand">
      <span class="brand__mark"></span>
      <span class="brand__name">Brivoldex.com</span>
    </div>
  </section>
</body>
</html>
```